Business Card/Design Project for Personal Injury Lawyer

Personal Injury Attorney. I represent people who have been injured in accidents and are making money damage claims against the negligent party. As a personal injury attorney, I am a counselor, advisor, and legal representative to my clients. Clients want someone who is aggresssive yet professional.

More information about what I do an be found at www.vorlandlaw.example

Target Market(s)

General public.

Industry/Entity Type

Legal

Contact Information for Business Card

Need a new logo/brand image for b-cards, website, and letterhead/envelops. Looking for something original (no scales of justice or courthouse columns), yet classy and professional.

Here's what I'm thinking (but I'm always open to other ideas):

On the front, I would like my name (Colton R. Vorland), and underneath the words "Personal Injury Attorney." The background could be black, for example, and the lettering could be white or foil. I'm open to differnt colors, or even two colors. My name on the front side should pop.

And then on the back would be all my contact info, and maybe a logo or a slogan.

Here are two slogans I've come up with so far: 1. Aim for Better. 2. Steady Advocacy for People Who Were Hurt.

Requirements
Must have
• Something that identifys me as a personal injury attorney, such as the words Personal Injury Attorney (or Lawyer, or Law Firm, etc.).
Nice to have
• A style/image that can be used nicely on my website and on letterhead.
Should not have
• Tired, commonly used logos or symbols, such a scales of justice or courthouse columns.

```html
<!DOCTYPE html>
<html lang="en">
<head>
<meta charset="utf-8">
<title>Vorland Law Business Card</title>
<link rel="stylesheet" href="https://fonts.googleapis.com/css2?family=Open+Sans:wght@400;600;700&display=swap">
<style>
  :root {
    --page: #ffffff;
    --card: #000000;
    --panel: #4a4a4a;
    --gold: #f3c24f;
    --mark-grey: #3a3a3a;
    --text-soft: #a9a9a9;
    --text-muted: #b8b8b8;
    --pill-bg: #3a3a3a;
    --pill-text: #b4b4b4;
  }
  * { margin: 0; padding: 0; box-sizing: border-box; }
  html, body {
    width: 1200px; height: 838px; overflow: hidden;
    background: var(--page);
    font-family: "Open Sans", Arial, sans-serif;
  }
  .canvas { position: relative; width: 1200px; height: 838px; }
  .card {
    position: absolute; left: 327px; width: 504px; height: 285px;
    background: var(--card);
    box-shadow: 6px 7px 8px rgba(0,0,0,0.35);
    overflow: hidden;
  }
  .card--front { top: 85px; text-align: center; }
  .card--back { top: 447px; }

  .brand-name {
    position: absolute; left: 0; right: 0; top: 61px;
    color: var(--mark-grey); font-weight: 700; font-size: 24px; letter-spacing: 1px;
    line-height: 32px;
  }
  .attorney-name {
    position: absolute; left: 0; right: 0; top: 138px;
    color: var(--gold); font-weight: 600; font-size: 26px;
  }
  .attorney-title {
    position: absolute; left: 0; right: 0; top: 176px;
    color: var(--text-soft); font-size: 13px;
  }
  .pill {
    position: absolute; background: var(--pill-bg); color: var(--pill-text);
    font-weight: 600; font-size: 13px; border-radius: 4px;
    padding: 2px 7px; white-space: nowrap;
  }
  .card--front .pill { left: 94px; top: 233px; width: 303px; text-align: center; }

  .side-panel {
    position: absolute; left: 0; top: 0; width: 102px; height: 100%;
    background: var(--panel);
  }
  .side-panel .brand-name {
    top: 44px; color: var(--gold); font-size: 15px; letter-spacing: 0.5px;
    line-height: 24px; text-align: center;
  }
  .firm-name {
    position: absolute; left: 121px; top: 48px;
    color: var(--text-soft); font-size: 28px; font-weight: 400;
  }
  .contact {
    position: absolute; left: 122px; top: 117px;
    list-style: none; color: var(--text-muted); font-size: 14px; line-height: 20.5px;
  }
  .card--back .pill { left: 117px; top: 223px; width: 124px; text-align: center; }
</style>
</head>
<body>
<main class="canvas">
  <section class="card card--front" aria-label="Business card front">
    <div class="brand-name">VORLAND</div>
    <h1 class="attorney-name">Colton R. Vorland</h1>
    <p class="attorney-title">Personal Injury Attorney</p>
    <p class="pill">Steady Advocacy for People Who Were Hurt</p>
  </section>

  <section class="card card--back" aria-label="Business card back">
    <div class="side-panel"><div class="brand-name">Vorland</div></div>
    <h2 class="firm-name">Vorland Law</h2>
    <ul class="contact">
      <li>305.555.0142</li>
      <li>www.vorlandlaw.example</li>
      <li>Free Consultation Available 24/7</li>
    </ul>
    <p class="pill">Aim for Better</p>
  </section>
</main>
</body>
</html>
```